RTV CRAFTED

building services
decks
pergola
renovation
extensions
general building

Target Market(s)

middle to upper class

Industry/Entity Type

building

Contact Information for Business Card

my details 0427839152 pkharlow47@mailvane.net BLD574926

Font styles to use
Serif

Colors
00AB8E
00BBA5
67D7C9
C6EFE9
E9F9F6

Requirements
Must have
• logo on the front and details on the back
Nice to have
• sharp and clean lines

```html
<!DOCTYPE html>
<html lang="en">
<head>
<meta charset="UTF-8">
<title>RTV Crafted – Business Card</title>
<link href="https://fonts.googleapis.com/css2?family=EB+Garamond:wght@400;500&display=swap" rel="stylesheet">
<style>
  :root {
    --teal: #00BBA5;
    --teal-deep: #00AB8E;
    --ink: #1a1a1a;
    --card-dark: #141414;
    --card-light: #ffffff;
    --backdrop: #e4e6e6;
  }
  * { margin: 0; padding: 0; box-sizing: border-box; }
  html, body {
    width: 1200px;
    height: 900px;
    overflow: hidden;
    background: var(--backdrop);
    font-family: "EB Garamond", Georgia, serif;
  }
  .canvas {
    position: relative;
    width: 1200px;
    height: 900px;
  }
  .card {
    position: absolute;
    left: 300px;
    width: 600px;
    height: 343px;
    border-radius: 22px;
    box-shadow: 0 10px 28px rgba(0,0,0,0.18);
    overflow: hidden;
  }
  .card--front {
    top: 92px;
    background: var(--card-dark);
    display: flex;
    align-items: center;
    justify-content: center;
  }
  .card--back {
    top: 465px;
    background: var(--card-light);
    color: var(--ink);
  }
  .brand-name {
    font-weight: 500;
    font-size: 50px;
    letter-spacing: 2px;
    line-height: 1;
    white-space: nowrap;
  }
  .card--front .brand-name { color: #ffffff; }
  .card--back .brand-name {
    position: absolute;
    top: 40px;
    left: 36px;
    font-size: 42px;
    color: var(--ink);
  }
  .contact-list {
    position: absolute;
    left: 36px;
    top: 196px;
    list-style: none;
    font-size: 17px;
    line-height: 1.4;
    letter-spacing: 0.5px;
  }
  .contact-list .label { color: var(--teal); margin-right: 6px; }
  .owner {
    position: absolute;
    right: 40px;
    top: 150px;
    text-align: right;
  }
  .owner-name {
    font-size: 22px;
    letter-spacing: 3px;
  }
  .owner-role {
    font-size: 15px;
    letter-spacing: 3px;
    color: var(--teal);
    margin-top: 2px;
  }
  .owner-rule {
    display: block;
    width: 40px;
    height: 2px;
    background: var(--ink);
    margin: 14px 0 0 auto;
  }
  .services {
    position: absolute;
    right: 40px;
    top: 232px;
    list-style: none;
    text-align: right;
    font-size: 13.5px;
    letter-spacing: 3.5px;
    line-height: 1.22;
    text-transform: uppercase;
  }
  .services .services-lead { margin-bottom: 6px; }
</style>
</head>
<body>
<main class="canvas">
  <section class="card card--front" aria-label="Card front">
    <span class="brand-name">RTV CRAFTED</span>
  </section>

  <section class="card card--back" aria-label="Card back">
    <span class="brand-name">RTV CRAFTED</span>

    <ul class="contact-list">
      <li><span class="label">P:</span>0427839152</li>
      <li><span class="label">E:</span>pkharlow47@mailvane.net</li>
      <li><span class="label">Lic No :</span>BLD574926</li>
    </ul>

    <div class="owner">
      <div class="owner-name">PETER HARLOW</div>
      <div class="owner-role">OWNER</div>
      <span class="owner-rule"></span>
    </div>

    <ul class="services">
      <li class="services-lead">Building Services</li>
      <li>Decks</li>
      <li>Pergola</li>
      <li>Renovation</li>
      <li>Extensions</li>
      <li>General Building</li>
    </ul>
  </section>
</main>
</body>
</html>
```